Etiketten für Tees
Zielgruppe
Wir sind eine klassische Foto-Drogerie mit traditioneller Likör Herstellung, Tee- und Gewürzstube mit offenen und selbst abgepackten Spezialitäten. Süßwarenabteilung mit Confiserie, großer Bonbon Auswahl und Drogerie Grundsortiment.
Wir suchen ein neues Etiketten Design für unsere selbst abgepackten Tees, Bonbons und Gewürze.
Aufgabenstellung
Die Etiketten für die Tees sollten durch verschiedene Farben oder Grafiken in die nachfolgenden Kategorien unterscheidbar sein: Schwarzer Tee, Grüner Tee, Früchte Tee, Rooibusch Tee und Kräuter Tee.
Abgefüllt sind die Tees in Blockbeutel Natron natur und die Früchtetees in Klarsichtbeutel.
Die Etiketten sollten etwa 65mm breit sein. die Länge kann zwischen 70mm und 110mm betragen.
Folgene Information müsste aufgedruckt werden: Art (Schwarzer Tee), Sorte (Darjeeling), kurze Beschreibung oder Geschmack (Erdbeer Geschmack), Füllmenge sowie unser Logo mit Adresse. Die Inhaltsstoffe, Zubereitung, Nährwerttabelle kommen in Text oder Tabellenform auf die Rückseite auf ein neutrales Etikett (hier nicht zu berücksichtigen).
Die Etiketten wollen wir mit unserem hochwertigen Vollfarb Etikettendrucker selbst ausdrucken (Drucker Velantis).
Das Design sollte auf die Natron Beutel farblich und von der Gestaltung her abgestimmt sein (natürliches und qualitativ hochwertiges Produkt - keine Massenware vom Discounter, jedoch trotzdem modern und 'nicht angestaubt spießig', aber nicht zu grelle Farben).
Wir möchten diese Etiketten im Sinne eines stimmigen Gesamtauftritts (sh. Foto) auch für unsere selbst abgepackten Bonbons und Gewürze verwenden. Es unterscheidet sich also nur marginal, d.h. in Bezeichnung und Füllmenge. Logo und Adresse bzw. das Gesamtbild sollen also gleich sein.

```html
<!DOCTYPE html>
<html lang="de">
<head>
<meta charset="utf-8">
<title>Teestube Kernhof – Tee-Etiketten</title>
<link href="https://fonts.googleapis.com/css2?family=Noto+Serif:wght@400;700&family=Yesteryear&display=swap" rel="stylesheet">
<style>
  :root {
    --canvas: #f1f1f1;
    --paper: #ffffff;
    --black: #1d1d1d;
    --text-dark: #1a1a1a;
    --fruit-band: #b79fd0;
    --fruit-ink: #6b2d8a;
    --rooibos-band: #e27bb8;
    --rooibos-ink: #c4157f;
    --green-band: #d6e4a8;
    --green-ink: #98bd25;
    --black-tea-band: #f0b266;
    --black-tea-ink: #e8870f;
    --herbal-band: #a3d0ad;
    --herbal-ink: #47a556;
  }
  * { box-sizing: border-box; margin: 0; padding: 0; }
  html, body {
    width: 1200px; height: 654px; overflow: hidden;
    background: var(--canvas);
  }
  .label-row {
    position: absolute; left: 25px; top: 214px;
    display: flex; gap: 25px;
  }
  .tea-label {
    position: relative; width: 210px; height: 226px;
    background: var(--paper);
    box-shadow: 0 1px 3px rgba(0,0,0,0.12);
    overflow: hidden;
    font-family: "Noto Serif", serif;
  }
  .tea-label--fruit { --band: var(--fruit-band); --ink: var(--fruit-ink); }
  .tea-label--rooibos { --band: var(--rooibos-band); --ink: var(--rooibos-ink); }
  .tea-label--green { --band: var(--green-band); --ink: var(--green-ink); }
  .tea-label--black { --band: var(--black-tea-band); --ink: var(--black-tea-ink); }
  .tea-label--herbal { --band: var(--herbal-band); --ink: var(--herbal-ink); }

  .swoosh { position: absolute; left: 0; top: 0; width: 210px; height: 193px; }
  .swoosh path { fill: var(--band); }

  .brand-box {
    position: absolute; left: 48px; top: 0; width: 114px; height: 66px;
    background: var(--black);
    display: flex; align-items: center; justify-content: center; gap: 6px;
  }
  .brand-name {
    color: var(--paper); font-family: "Noto Serif", serif;
    font-size: 15px; font-weight: 400; letter-spacing: 0.5px;
  }
  .brand-dot { width: 7px; height: 7px; border-radius: 50%; background: var(--paper); }

  .tea-category {
    position: absolute; left: 27px; top: 90px;
    font-size: 8.5px; font-weight: 700; letter-spacing: 1.4px;
    color: var(--text-dark); text-transform: uppercase;
  }
  .tea-variety {
    position: absolute; left: 0; right: 0; top: 100px;
    text-align: center; font-family: "Yesteryear", cursive;
    font-size: 40px; line-height: 1; color: var(--black);
    transform: rotate(-9deg); padding-left: 14px;
  }
  .tea-description {
    position: absolute; right: 20px; top: 151px;
    text-align: right; font-size: 9.5px; line-height: 1.15; color: var(--ink);
  }
  .tea-weight {
    position: absolute; right: 20px; top: 176px;
    font-size: 9.5px; font-weight: 700; color: var(--text-dark);
  }
  .contact-bar {
    position: absolute; left: 0; bottom: 0; width: 100%; height: 32px;
    background: var(--black); color: var(--paper);
    display: flex; flex-direction: column; align-items: center; justify-content: center;
    font-size: 6px; line-height: 1.45;
  }
  .contact-web { font-weight: 700; letter-spacing: 0.3px; }
</style>
</head>
<body>
<main class="label-row">

  <article class="tea-label tea-label--fruit">
    <svg class="swoosh" viewBox="0 0 210 193" aria-hidden="true">
      <path d="M0,40 C70,58 140,68 210,66 L210,104 C140,104 70,118 0,138 Z" opacity="0.45"/>
      <path d="M0,72 C70,80 140,84 210,80 L210,98 C140,100 70,110 0,122 Z" opacity="0.8"/>
    </svg>
    <div class="brand-box"><span class="brand-name">Kernhof</span><span class="brand-dot"></span></div>
    <p class="tea-category">Früchte Tee</p>
    <h2 class="tea-variety">Waldfrucht</h2>
    <p class="tea-description" style="top:163px">Brombeere-Hagebute</p>
    <p class="tea-weight">200g</p>
    <footer class="contact-bar"><span>Lindenweg 7 · 12345 Musterstadt · Tel. +49 1234-5678</span><span class="contact-web">www.kernhof-tee.de</span></footer>
  </article>

  <article class="tea-label tea-label--rooibos">
    <svg class="swoosh" viewBox="0 0 210 193" aria-hidden="true">
      <path d="M0,40 C70,58 140,68 210,66 L210,104 C140,104 70,118 0,138 Z" opacity="0.45"/>
      <path d="M0,72 C70,80 140,84 210,80 L210,98 C140,100 70,110 0,122 Z" opacity="0.8"/>
    </svg>
    <div class="brand-box"><span class="brand-name">Kernhof</span><span class="brand-dot"></span></div>
    <p class="tea-category">Rooibusch Tee</p>
    <h2 class="tea-variety">Vanille</h2>
    <p class="tea-description">Roibusch-Tee<br>mit Vanille Geschmack</p>
    <p class="tea-weight">200g</p>
    <footer class="contact-bar"><span>Lindenweg 7 · 12345 Musterstadt · Tel. +49 1234-5678</span><span class="contact-web">www.kernhof-tee.de</span></footer>
  </article>

  <article class="tea-label tea-label--green">
    <svg class="swoosh" viewBox="0 0 210 193" aria-hidden="true">
      <path d="M0,40 C70,58 140,68 210,66 L210,104 C140,104 70,118 0,138 Z" opacity="0.45"/>
      <path d="M0,72 C70,80 140,84 210,80 L210,98 C140,100 70,110 0,122 Z" opacity="0.8"/>
    </svg>
    <div class="brand-box"><span class="brand-name">Kernhof</span><span class="brand-dot"></span></div>
    <p class="tea-category">Grüner Tee</p>
    <h2 class="tea-variety">Rosentraum</h2>
    <p class="tea-description">mit getrockneten<br>Rosenblüten</p>
    <p class="tea-weight">200g</p>
    <footer class="contact-bar"><span>Lindenweg 7 · 12345 Musterstadt · Tel. +49 1234-5678</span><span class="contact-web">www.kernhof-tee.de</span></footer>
  </article>

  <article class="tea-label tea-label--black">
    <svg class="swoosh" viewBox="0 0 210 193" aria-hidden="true">
      <path d="M0,40 C70,58 140,68 210,66 L210,104 C140,104 70,118 0,138 Z" opacity="0.45"/>
      <path d="M0,72 C70,80 140,84 210,80 L210,98 C140,100 70,110 0,122 Z" opacity="0.8"/>
    </svg>
    <div class="brand-box"><span class="brand-name">Kernhof</span><span class="brand-dot"></span></div>
    <p class="tea-category">Schwarzer Tee</p>
    <h2 class="tea-variety">Darjeeling</h2>
    <p class="tea-description" style="top:163px">mit Vanille-Geschmack</p>
    <p class="tea-weight">200g</p>
    <footer class="contact-bar"><span>Lindenweg 7 · 12345 Musterstadt · Tel. +49 1234-5678</span><span class="contact-web">www.kernhof-tee.de</span></footer>
  </article>

  <article class="tea-label tea-label--herbal">
    <svg class="swoosh" viewBox="0 0 210 193" aria-hidden="true">
      <path d="M0,40 C70,58 140,68 210,66 L210,104 C140,104 70,118 0,138 Z" opacity="0.45"/>
      <path d="M0,72 C70,80 140,84 210,80 L210,98 C140,100 70,110 0,122 Z" opacity="0.8"/>
    </svg>
    <div class="brand-box"><span class="brand-name">Kernhof</span><span class="brand-dot"></span></div>
    <p class="tea-category">Kräuter Tee</p>
    <h2 class="tea-variety">Minze</h2>
    <p class="tea-description">wohltuend<br>für Geist &amp; Seele</p>
    <p class="tea-weight">200g</p>
    <footer class="contact-bar"><span>Lindenweg 7 · 12345 Musterstadt · Tel. +49 1234-5678</span><span class="contact-web">www.kernhof-tee.de</span></footer>
  </article>

</main>
</body>
</html>
```